Peach Point of Sale Cards for Grocery Retail Markets

We are looking to update our peach point of sale card and price card. The cards will need to be 7" x 11" with a .125 bleed - one sided. See attached for the old versions. We would like this to use photos that look like true Washington State Peaches. Here are the bullet points we would like to use: - New Crop!- Tree Ripened- Excellent FlavorNOTE: The price card just needs to have a space where a retailer can write in the sale price of the item. See attachment with the white box.

Target Market(s)

Retail market shoppers

Requirements
Must have
• Pictures of Peaches Only

```html
<!DOCTYPE html>
<html lang="en">
<head>
<meta charset="utf-8">
<title>Peach Price Card</title>
<link rel="stylesheet" href="https://fonts.googleapis.com/css2?family=Anton&family=Open+Sans:wght@700&family=Yellowtail&family=Montserrat:wght@900&display=block">
<style>
  :root {
    --stage: #000000;
    --green: #0b6b3a;
    --white: #ffffff;
    --badge: #f3be2b;
    --peach-light: #f7a94a;
    --peach-mid: #ef7d3a;
    --peach-red: #d9453a;
    --band: rgba(250, 170, 80, 0.55);
    --tick: #7a1e22;
    --string: #cfd3d6;
  }
  * { margin: 0; padding: 0; box-sizing: border-box; }
  html, body { width: 1200px; height: 1200px; overflow: hidden; background: var(--stage); }
  .card {
    position: absolute; left: 201px; top: 345px; width: 799px; height: 510px;
    overflow: hidden;
  }
  .peach-photo {
    position: absolute; inset: 0;
    background:
      radial-gradient(circle at 35% 45%, var(--peach-red) 0, transparent 30%),
      radial-gradient(circle at 75% 55%, var(--peach-red) 0, transparent 25%),
      radial-gradient(circle at 10% 75%, var(--peach-mid) 0, transparent 30%),
      linear-gradient(135deg, var(--peach-light), var(--peach-mid) 55%, var(--peach-light));
  }
  .band { position: absolute; left: 0; width: 100%; background: var(--band); }
  .band-top { top: 0; height: 114px; }
  .band-bottom { top: 395px; height: 115px; }
  .title {
    position: absolute; top: 22px; left: 0; width: 100%; text-align: center;
    white-space: nowrap;
    font-family: "Anton", sans-serif; font-weight: 400; font-size: 66px; line-height: 1; color: var(--green);
    text-shadow: 2px 2px 0 var(--white), -2px -2px 0 var(--white), 2px -2px 0 var(--white), -2px 2px 0 var(--white), 3px 4px 6px rgba(0,0,0,.4);
  }
  .badge { position: absolute; left: 37px; top: 128px; width: 186px; height: 186px; }
  .badge-new {
    position: absolute; left: 0; top: 30px; width: 100%; text-align: center;
    font-family: "Yellowtail", cursive; font-size: 72px; line-height: 1; color: var(--white);
    transform: rotate(-12deg); text-shadow: 2px 3px 4px rgba(0,0,0,.35);
  }
  .badge-crops {
    position: absolute; left: 30px; top: 106px; width: 140px; text-align: center;
    font-family: "Montserrat", sans-serif; font-weight: 900; font-size: 30px; line-height: 1; color: var(--white);
    transform: rotate(-16deg); text-shadow: 2px 3px 4px rgba(0,0,0,.35);
  }
  .benefits { position: absolute; left: 248px; top: 156px; list-style: none; }
  .benefit {
    display: flex; align-items: center; height: 66px; white-space: nowrap;
    font-family: "Anton", sans-serif; font-size: 46px; line-height: 1; color: var(--green);
    text-shadow: 2px 2px 0 var(--white), -1px -1px 0 var(--white), 2px -1px 0 var(--white), -1px 2px 0 var(--white), 2px 4px 5px rgba(0,0,0,.4);
  }
  .benefit svg { width: 42px; height: 42px; margin-right: 12px; flex: none; }
  .price-tag { position: absolute; left: 0; top: 0; width: 799px; height: 510px; }
  .sponsor { position: absolute; left: 45px; top: 409px; display: flex; align-items: center; }
  .sponsor-dot { width: 84px; height: 84px; border-radius: 50%; background: var(--peach-red); margin-right: 22px; }
  .sponsor-name {
    font-family: "Open Sans", sans-serif; font-weight: 700; font-size: 22px; line-height: 24px; color: var(--green);
  }
</style>
</head>
<body>
  <main class="card">
    <div class="peach-photo" role="img" aria-label="Close-up photo of ripe Washington peaches piled together"></div>
    <div class="band band-top"></div>
    <div class="band band-bottom"></div>

    <h1 class="title">Washington State Peaches</h1>

    <div class="badge">
      <svg width="186" height="186" viewBox="0 0 186 186">
        <circle cx="93" cy="93" r="82" fill="var(--badge)"/>
        <circle cx="93" cy="93" r="84" fill="none" stroke="var(--badge)" stroke-width="16" stroke-linecap="round" stroke-dasharray="0 22"/>
      </svg>
      <div class="badge-new">New</div>
      <div class="badge-crops">CROPS</div>
    </div>

    <ul class="benefits">
      <li class="benefit">
        <svg viewBox="0 0 42 42"><circle cx="21" cy="21" r="20" fill="var(--white)"/><path d="M11 21 L18 29 L31 11" fill="none" stroke="var(--tick)" stroke-width="3.5" stroke-linecap="round" stroke-linejoin="round"/></svg>
        Tree Ripened
      </li>
      <li class="benefit">
        <svg viewBox="0 0 42 42"><circle cx="21" cy="21" r="20" fill="var(--white)"/><path d="M11 21 L18 29 L31 11" fill="none" stroke="var(--tick)" stroke-width="3.5" stroke-linecap="round" stroke-linejoin="round"/></svg>
        Excellent Flavor
      </li>
    </ul>

    <svg class="price-tag" viewBox="0 0 799 510" aria-label="Blank price tag for writing in the sale price">
      <circle cx="561" cy="453" r="152" fill="var(--white)" stroke="#e2e2e2" stroke-width="3"/>
      <circle cx="622" cy="369" r="17" fill="#efe3c8"/>
      <circle cx="622" cy="369" r="9" fill="#1d2430"/>
      <path d="M622 369 C660 330 700 290 760 280 C790 276 780 305 750 310 C710 318 670 340 622 369" fill="none" stroke="var(--string)" stroke-width="4"/>
      <path d="M622 369 C670 320 730 260 770 275" fill="none" stroke="var(--string)" stroke-width="4"/>
    </svg>

    <div class="sponsor">
      <div class="sponsor-dot"></div>
      <div class="sponsor-name">Cascade Orchard<br>Growers Council</div>
    </div>
  </main>
</body>
</html>
```